Business Card Design

My business is writing crime novels to entertain readers. I write legal thrillers and mysteries. I need a card for publishers, agents, other authors, and media.

Industry/Entity Type

Legal

Contact Information for Business Card

Paul Trenholt
www.trenholtnoir.example
pbtrenholt@mailbox.example
0064 27 5170942

```html
<!DOCTYPE html>
<html lang="en">
<head>
<meta charset="utf-8">
<title>Paul Trenholt — Business Card</title>
<link href="https://fonts.googleapis.com/css2?family=Comfortaa:wght@400;500;600&display=swap" rel="stylesheet">
<style>
  :root {
    --backdrop: #e6e6e8;
    --card: #ffffff;
    --ink-dark: #3b4048;
    --ink-mid: #5a5e66;
    --ink-soft: #8c9096;
    --band-dark: #676a73;
    --band-mid: #9a9da3;
    --band-light: #d4d5d8;
    --rule: #9ea1a7;
    --portrait-dark: #2f3034;
    --portrait-mid: #8f8b88;
    --portrait-light: #ecebea;
  }
  * { box-sizing: border-box; margin: 0; padding: 0; }
  html, body {
    width: 1200px;
    height: 1200px;
    overflow: hidden;
  }
  body {
    background: var(--backdrop);
    font-family: "Comfortaa", sans-serif;
    position: relative;
  }
  .business-card {
    position: absolute;
    left: 100px;
    top: 314px;
    width: 1000px;
    height: 572px;
    background: var(--card);
    overflow: hidden;
    box-shadow: 0 10px 30px rgba(0,0,0,0.12);
  }
  .accent-rule {
    position: absolute;
    left: 0;
    top: 0;
    width: 1000px;
    height: 572px;
  }
  .identity {
    position: absolute;
    left: 88px;
    top: 66px;
  }
  .identity__name {
    font-size: 46px;
    font-weight: 500;
    color: var(--ink-dark);
    letter-spacing: 0.5px;
  }
  .identity__role {
    font-size: 25px;
    font-weight: 400;
    color: var(--ink-soft);
    margin-top: 6px;
    margin-left: 2px;
  }
  .contact {
    position: absolute;
    left: 90px;
    top: 224px;
    line-height: 1.45;
  }
  .contact__phone {
    font-size: 27px;
    color: var(--ink-mid);
  }
  .contact__email {
    font-size: 25px;
    color: var(--ink-soft);
  }
  .web-band {
    position: absolute;
    left: 0;
    top: 340px;
    width: 760px;
    height: 118px;
    background: linear-gradient(90deg, var(--band-dark) 0%, var(--band-mid) 55%, var(--band-light) 85%, rgba(255,255,255,0) 100%);
    display: flex;
    align-items: center;
    padding-left: 92px;
  }
  .web-band__url {
    font-size: 36px;
    font-weight: 500;
    color: #ffffff;
    letter-spacing: 0.5px;
  }
  .portrait {
    position: absolute;
    left: 600px;
    top: 120px;
    width: 400px;
    height: 452px;
    background:
      radial-gradient(ellipse 40% 30% at 55% 25%, var(--portrait-mid) 0%, rgba(143,139,136,0) 100%),
      radial-gradient(ellipse 75% 55% at 55% 100%, var(--portrait-dark) 0%, var(--portrait-dark) 45%, rgba(47,48,52,0) 100%),
      linear-gradient(180deg, var(--card) 0%, var(--portrait-light) 100%);
  }
</style>
</head>
<body>
  <section class="business-card">
    <svg class="accent-rule" viewBox="0 0 1000 572" aria-hidden="true">
      <defs>
        <linearGradient id="ruleFade" x1="0" y1="0" x2="1" y2="0">
          <stop offset="0" stop-color="#9ea1a7" stop-opacity="1"/>
          <stop offset="0.7" stop-color="#9ea1a7" stop-opacity="0.6"/>
          <stop offset="1" stop-color="#9ea1a7" stop-opacity="0"/>
        </linearGradient>
      </defs>
      <polygon points="0,172 680,206 680,208 0,178" fill="url(#ruleFade)"/>
    </svg>

    <div class="identity">
      <h1 class="identity__name">Paul Trenholt</h1>
      <p class="identity__role">Writer</p>
    </div>

    <div class="contact">
      <p class="contact__phone">0064 27 5170942</p>
      <p class="contact__email">pbtrenholt@mailbox.example</p>
    </div>

    <div class="web-band">
      <p class="web-band__url">www.trenholtnoir.example</p>
    </div>

    <div class="portrait" role="img" aria-label="Portrait photo of the author in a white shirt and dark leather jacket"></div>
  </section>
</body>
</html>
```